Business Card Design

We would like a business card that utilizes our current logo and keeps with the same feel - elegant and organic. Our farm isn't about mass production, it's about excellence, education, beautiful events and flowers - people, culture, and community.

Target Market(s)

Patrons to our farm who are interested in weddings, events, or our flowers and vegetables.

Contact Information for Business Card

Name, address, cell email (Danielle Hoskins, 2716 Wrenfield Rd, Brindlewood, CO 80617, cell 30.412.6638, email danielle@wrenfieldacres.com)

```html
<!DOCTYPE html>
<html lang="en">
<head>
<meta charset="utf-8">
<title>Wrenfield Acres — Business Card</title>
<link rel="stylesheet" href="https://fonts.googleapis.com/css2?family=Quicksand:wght@400;500;700&family=Arimo:wght@700&display=swap">
<style>
  :root {
    --backdrop: #c9c9cb;
    --paper: #ffffff;
    --sage: #798a77;
    --sage-text: #6f8470;
    --tan: #a57d55;
  }
  * { margin: 0; padding: 0; box-sizing: border-box; }
  html, body {
    width: 1200px; height: 1200px; overflow: hidden;
    background: var(--backdrop);
  }
  .card {
    position: absolute;
    left: 232px;
    width: 718px;
    height: 410px;
    background: var(--paper);
    overflow: hidden;
  }
  .card--front { top: 185px; }
  .card--back { top: 649px; }

  .wordmark {
    position: absolute;
    font-family: "Quicksand", sans-serif;
    font-weight: 500;
    white-space: nowrap;
    transform: translateX(-50%);
    letter-spacing: 0.02em;
  }
  .card--front .wordmark {
    left: 363px; top: 168px;
    font-size: 47px;
    color: var(--sage);
  }
  .card--back .wordmark {
    left: 588px; top: 328px;
    font-size: 26px;
    color: var(--paper);
    z-index: 2;
  }

  .card-shape {
    position: absolute; inset: 0;
    width: 100%; height: 100%;
  }

  .holder-name {
    position: absolute;
    left: 52px; top: 74px;
    font-family: "Quicksand", sans-serif;
    font-size: 45px;
    font-weight: 400;
    color: var(--sage-text);
    white-space: nowrap;
  }
  .holder-name strong { font-weight: 700; }

  .contact-list {
    position: absolute;
    left: 53px; top: 194px;
    list-style: none;
    font-family: "Arimo", sans-serif;
    font-weight: 700;
    font-size: 15.5px;
    color: var(--sage-text);
  }
  .contact-list li {
    display: flex;
    align-items: flex-start;
    line-height: 31px;
  }
  .contact-list .icon {
    width: 16px; height: 16px;
    margin-top: 7px;
    margin-right: 12px;
    flex: none;
    fill: var(--sage-text);
  }
  .address-lines { display: block; }
</style>
</head>
<body>

<section class="card card--front" aria-label="Business card front">
  <div class="wordmark">Wrenfield Acres</div>
</section>

<section class="card card--back" aria-label="Business card back">
  <svg class="card-shape" viewBox="0 0 598 342" preserveAspectRatio="none" aria-hidden="true">
    <rect width="598" height="342" fill="var(--sage)"/>
    <path d="M0 0 H338 C445 22 482 92 452 152 C428 222 322 292 228 342 H0 Z" fill="var(--tan)"/>
    <path d="M0 0 H328 C420 22 462 88 430 150 C402 220 300 290 205 342 H0 Z" fill="var(--paper)"/>
  </svg>

  <h1 class="holder-name">Danielle <strong>Hoskins</strong></h1>

  <ul class="contact-list">
    <li>
      <svg class="icon" viewBox="0 0 16 16" aria-hidden="true"><path d="M8 0a5.5 5.5 0 0 0-5.5 5.5C2.5 9.6 8 16 8 16s5.5-6.4 5.5-10.5A5.5 5.5 0 0 0 8 0zm0 7.7a2.2 2.2 0 1 1 0-4.4 2.2 2.2 0 0 1 0 4.4z"/></svg>
      <span class="address-lines">2716 Wrenfield Rd, Brindlewood,<br>CO 80617</span>
    </li>
    <li>
      <svg class="icon" viewBox="0 0 16 16" aria-hidden="true"><path d="M3.6 1.2 5.7 3.6c.4.4.3 1-.1 1.4L4.5 6c.8 1.9 2.6 3.7 4.5 4.5l1-1.1c.4-.4 1-.5 1.4-.1l2.4 2.1c.4.4.4 1 0 1.4l-1.3 1.3C11 15.4 6.9 13.6 4.6 11.4 2.4 9.1.6 5 1.9 3.6L3.2 2.3c.2-.2.3-.6.4-1.1z"/></svg>
      <span>30.412.6638</span>
    </li>
    <li>
      <svg class="icon" viewBox="0 0 16 16" aria-hidden="true"><path d="M1 3.5h14v1L8 9 1 4.5zM1 6l7 4.4L15 6v6.5H1z"/></svg>
      <span>danielle@wrenfieldacres.com</span>
    </li>
  </ul>

  <div class="wordmark">Wrenfield Acres</div>
</section>

</body>
</html>
```